Law Firm Corporate Identity Package

Stationery, fax, and business card.
Updates

Name of firm is "Halvorsen Law PC."

Target Market(s)

Real estate investor clients

Industry/Entity Type

Legal

Font styles to use
Serif

Colors
3277b5
85acd3

```html
<!DOCTYPE html>
<html lang="en">
<head>
<meta charset="utf-8">
<title>Halvorsen Law PC — Stationery Set</title>
<link href="https://fonts.googleapis.com/css2?family=Cinzel:wght@500&family=Libre+Baskerville:wght@400;700&family=Open+Sans:wght@400;600&display=swap" rel="stylesheet">
<style>
  :root{
    --brand:#3277b5;
    --brand-light:#85acd3;
    --brand-deep:#2a67a0;
    --emboss:#2c6aa3;
    --paper:#ffffff;
    --ink:#222;
    --muted:#666;
    --bg-1:#ececec;
    --bg-2:#d9d9d9;
    --bg-3:#efefef;
    --bg-4:#e6e6e6;
  }
  *{box-sizing:border-box;margin:0;padding:0}
  html,body{width:1200px;height:3000px;overflow:hidden}
  body{position:relative;font-family:"Libre Baskerville",Georgia,serif;color:var(--ink)}
  .section{position:absolute;left:0;width:1200px}
  .s1{top:0;height:820px;background:var(--bg-1)}
  .s2{top:820px;height:820px;background:var(--bg-2)}
  .s3{top:1640px;height:820px;background:var(--bg-3)}
  .s4{top:2460px;height:540px;background:var(--bg-4)}
  .piece{position:absolute;box-shadow:0 2px 6px rgba(0,0,0,.12)}
  .blue{background:var(--brand)}
  .white{background:var(--paper)}
  .wordmark{font-family:"Cinzel",Georgia,serif;font-weight:500;letter-spacing:.06em;text-transform:uppercase;text-align:center;line-height:1.15}
  .wordmark.on-blue{color:var(--emboss)}
  .wordmark.on-white{color:var(--brand)}
  .band{position:absolute;left:0;right:0;background:var(--brand)}
  .tiny{font-family:"Open Sans",Arial,sans-serif;font-size:6px;color:var(--muted)}
  .body-copy{font-size:6.5px;line-height:1.55;color:#444;text-align:justify}
  .body-copy p{margin-bottom:6px}
  /* business card large */
  .card-name{font-family:"Open Sans",Arial,sans-serif;font-weight:600;font-size:24px;color:#111}
  .card-role{font-family:"Open Sans",Arial,sans-serif;font-size:15px;color:var(--brand)}
  .card-info{font-family:"Open Sans",Arial,sans-serif;font-size:13px;line-height:1.45;color:#222;margin-top:10px}
  /* letter 1 */
  .letter{font-size:6.6px;line-height:1.45;color:#111}
  .letter p{margin-bottom:6px}
  .price-table{width:100%;border-collapse:collapse;font-size:5.5px;color:#444;margin:6px 0 8px}
  .price-table td{border-bottom:1px solid #bbb;padding:2px 0}
  .price-table td:last-child{text-align:right}
  .notebook-strap{position:absolute;top:0;bottom:0;width:16px;background:var(--brand-deep)}
</style>
</head>
<body>

<!-- Section 1: full set overview -->
<section class="section s1">
  <div class="piece blue folder" style="left:70px;top:50px;width:450px;height:590px">
    <div class="wordmark on-blue" style="margin-top:90px;font-size:30px">Halvorsen<br><span style="font-size:18px">Law PC</span></div>
  </div>

  <div class="piece white letterhead" style="left:560px;top:50px;width:400px;height:540px">
    <div class="wordmark on-white" style="position:absolute;right:40px;top:26px;font-size:12px">Halvorsen<br><span style="font-size:8px">Law PC</span></div>
    <div class="body-copy" style="position:absolute;left:40px;right:40px;top:80px">
      <p>Thank you for choosing our firm to guide your next property purchase. We have reviewed the contract and title documents you provided, and we are pleased to confirm that the transaction can proceed on the timetable discussed at our meeting last week.</p>
      <p>Before settlement we will need signed copies of the enclosed forms, proof of funds from your lender and a short note confirming how the property will be held. Our team will contact the vendor's representative directly.</p>
      <p>Should anything change with your finance or the building inspection, please let us know at once so that we may protect your position under the special conditions.</p>
      <p>We look forward to working with you.</p>
    </div>
    <div class="band" style="bottom:18px;height:6px"></div>
    <div class="tiny" style="position:absolute;bottom:30px;width:100%;text-align:center">12/60 Harbourview Road, Kelton QLD 4170</div>
  </div>

  <div class="piece blue card-back" style="left:150px;top:668px;width:200px;height:116px">
    <div class="wordmark on-blue" style="margin-top:40px;font-size:12px">Halvorsen<br><span style="font-size:8px">Law PC</span></div>
  </div>
  <div class="piece white card-front" style="left:370px;top:668px;width:200px;height:116px">
    <div class="wordmark on-white" style="position:absolute;right:14px;top:12px;font-size:8px">Halvorsen<br><span style="font-size:6px">Law PC</span></div>
    <div class="tiny" style="position:absolute;left:14px;top:42px;line-height:1.4;color:#333">Marcus Ellery<br>Director<br>Tel +1300 555 010</div>
    <div class="band" style="bottom:0;height:10px"></div>
  </div>

  <div class="piece white envelope" style="left:660px;top:620px;width:460px;height:170px">
    <div class="wordmark on-white" style="position:absolute;right:30px;top:16px;font-size:11px">Halvorsen<br><span style="font-size:7px">Law PC</span></div>
    <div class="band" style="top:78px;height:8px"></div>
    <div class="band" style="top:96px;height:26px"></div>
  </div>
</section>

<!-- Section 2: business card -->
<section class="section s2">
  <div class="piece blue card-back-lg" style="left:620px;top:70px;width:500px;height:290px">
    <div class="wordmark on-blue" style="margin-top:100px;font-size:34px">Halvorsen<br><span style="font-size:22px">Law PC</span></div>
  </div>
  <div class="piece white card-front-lg" style="left:90px;top:220px;width:560px;height:320px">
    <div class="wordmark on-white" style="position:absolute;right:32px;top:28px;font-size:22px">Halvorsen<br><span style="font-size:14px">Law PC</span></div>
    <div style="position:absolute;left:34px;top:120px">
      <div class="card-name">Marcus Ellery</div>
      <div class="card-role">Director</div>
      <div class="card-info">12/60 Harbourview Road, Kelton QLD 4170<br>info@halvorsenlaw.com<br>Tel +1300 555 010<br>Fax 0400 555 019<br>www.halvorsenlaw.com</div>
    </div>
    <div class="band" style="bottom:0;height:30px"></div>
  </div>
</section>

<!-- Section 3: envelopes, letterheads, folder -->
<section class="section s3">
  <div class="piece white envelope-back" style="left:210px;top:50px;width:350px;height:180px">
    <svg width="350" height="60" style="position:absolute;top:0;left:0" aria-hidden="true"><polygon points="0,0 350,0 330,55 20,55" fill="#3277b5"/></svg>
    <div class="wordmark on-blue" style="position:relative;margin-top:14px;font-size:11px;color:#1f4f7a">Halvorsen<br><span style="font-size:7px">Law PC</span></div>
  </div>
  <div class="piece white envelope-front" style="left:640px;top:50px;width:350px;height:180px">
    <div class="wordmark on-white" style="position:absolute;left:20px;top:20px;font-size:11px">Halvorsen<br><span style="font-size:7px">Law PC</span></div>
    <div class="tiny" style="position:absolute;left:16px;bottom:16px">12/60 Harbourview Road, Kelton QLD 4170</div>
    <div class="band" style="bottom:0;height:7px"></div>
  </div>

  <div class="piece white letterhead-a" style="left:25px;top:280px;width:350px;height:480px">
    <div class="wordmark" style="margin-top:22px;font-size:12px;color:#111">Halvorsen<br><span style="font-size:8px">Law PC</span></div>
    <div style="margin:6px 26px 0;height:2px;background:#111"></div>
    <div class="letter" style="padding:14px 26px 0">
      <p>May 30, 2006</p>
      <p>Dana Whitfield<br>8810 Lakeside Drive<br>Chicago, IL 60611</p>
      <p>Dear Ms. Whitfield:</p>
      <p><b>Our team is pleased to confirm your settlement date.</b></p>
      <p>We have completed the title search and the survey report, and both are clear of any concern. The vendor has agreed to the revised terms and signed the amended contract.</p>
      <p>Please review the enclosed statement of adjustments and return the signed authority at your earliest convenience so that funds can be arranged with your lender.</p>
      <p>If you have any questions about the process, our office is open each weekday and we are always happy to help.</p>
      <p>Regards,</p>
      <p>Nora Pell</p>
    </div>
    <div class="band" style="bottom:0;height:8px;background:#111"></div>
    <div class="tiny" style="position:absolute;bottom:12px;width:100%;text-align:center">12/60 Harbourview Road, Kelton QLD 4170 · 1300 555 010</div>
  </div>

  <div class="piece white letterhead-b" style="left:405px;top:280px;width:350px;height:480px">
    <div class="wordmark on-white" style="margin-top:20px;font-size:12px">Halvorsen<br><span style="font-size:8px">Law PC</span></div>
    <div class="body-copy" style="padding:18px 26px 0">
      <p>Please find below a summary of the fees for your recent property matter. All amounts are shown in full and include the searches we lodged on your behalf.</p>
      <p>Payment may be made by transfer within fourteen days. Contact our accounts team with any query regarding this notice.</p>
      <table class="price-table">
        <tr><td>Contract review</td><td>$95.00</td></tr>
        <tr><td>Title search</td><td>$60.00</td></tr>
        <tr><td>Council search</td><td>$45.00</td></tr>
        <tr><td>Settlement attendance</td><td>$80.00</td></tr>
        <tr><td>Lodgement fee</td><td>$35.00</td></tr>
        <tr><td>Total due</td><td>$315.00</td></tr>
      </table>
      <p>Thank you for your continued trust in our firm.</p>
    </div>
    <div class="band" style="bottom:0;height:7px"></div>
    <div class="tiny" style="position:absolute;bottom:12px;width:100%;text-align:center">12/60 Harbourview Road, Kelton QLD 4170 · www.halvorsenlaw.com</div>
  </div>

  <div class="piece blue folder-sm" style="left:790px;top:270px;width:370px;height:500px">
    <div class="wordmark on-blue" style="margin-top:190px;font-size:24px">Halvorsen<br><span style="font-size:16px">Law PC</span></div>
  </div>
</section>

<!-- Section 4: notebook and lockup -->
<section class="section s4">
  <div class="piece blue notebook" style="left:90px;top:50px;width:420px;height:440px;border-radius:6px">
    <div class="notebook-strap" style="left:330px"></div>
    <div class="wordmark on-blue" style="margin-top:150px;margin-right:80px;font-size:26px">Halvorsen<br><span style="font-size:17px">Law PC</span></div>
  </div>
  <div class="wordmark on-white lockup" style="position:absolute;left:640px;top:200px;width:480px;font-size:40px">Halvorsen<br><span style="font-size:26px">Law PC</span></div>
</section>

</body>
</html>
```